Redesign of existing business card

I would like the "signage" attachment converted into a business card. This needs to be double sided aswell, keeping the phone number and names on the front, and the email + website on the back.

Second attachment is the current business card design.

Larger font for contact details is required.

Must keep to original color themes (electric blue, silver/grey etc)

Back of the card to have blue background with white writing.

Industry/Entity Type

Business

Contact Information for Business Card

Refer to existing design from attachments

Requirements
Must have
• Refer to existing design from attachments
Nice to have

```html
<!DOCTYPE html>
<html lang="en">
<head>
<meta charset="utf-8">
<title>Voltra Power Services – Business Card</title>
<link rel="stylesheet" href="https://fonts.googleapis.com/css2?family=Cinzel:wght@700&family=Open+Sans:wght@400;700&family=Arimo:wght@400&display=swap">
<style>
  :root {
    --electric-blue: #0a0af5;
    --card-white: #ffffff;
    --ink: #222222;
    --stage: #ececec;
    --border-dark: #1a1a1a;
  }
  * { margin: 0; padding: 0; box-sizing: border-box; }
  html, body { width: 1200px; height: 2454px; overflow: hidden; background: var(--stage); }
  .canvas { position: relative; width: 1200px; height: 2454px; background: var(--stage); }

  .card { position: absolute; left: 0; width: 1200px; overflow: hidden; }
  .card--front { top: 0; height: 687px; background: var(--card-white); }
  .card--back {
    top: 687px; height: 688px; background: var(--electric-blue);
    border: 2px solid var(--border-dark);
  }

  .card__shapes { position: absolute; inset: 0; }

  .brand {
    position: absolute; left: 30px; top: 40px;
    font-family: "Open Sans", sans-serif; font-weight: 700;
    color: var(--electric-blue); line-height: 1;
  }
  .brand__primary { display: block; font-size: 190px; letter-spacing: 6px; }
  .brand__secondary { display: block; font-size: 66px; letter-spacing: 5px; margin-top: 8px; }

  .holder { position: absolute; left: 147px; top: 405px; }
  .holder__name {
    font-family: "Cinzel", serif; font-weight: 700;
    font-size: 84px; color: var(--ink); line-height: 1; letter-spacing: 1px;
  }
  .holder__location {
    font-family: "Open Sans", sans-serif; font-size: 27px;
    color: var(--ink); letter-spacing: 3px; margin: 14px 0 0 58px;
  }
  .holder__phone {
    font-family: "Open Sans", sans-serif; font-size: 24px;
    color: var(--ink); margin: 14px 0 0 135px;
  }

  .contact {
    position: absolute; left: 0; right: 0; top: 218px;
    text-align: center; color: var(--card-white);
  }
  .contact__email {
    font-family: "Open Sans", sans-serif; font-weight: 400;
    font-size: 68px; letter-spacing: 2px; line-height: 1.2; padding-left: 30px;
  }
  .contact__rule {
    width: 696px; height: 2px; background: var(--card-white);
    margin: 2px 0 0 270px;
  }
  .contact__web {
    font-family: "Arimo", sans-serif; font-size: 36px;
    margin-top: 6px; margin-left: -10px;
  }
</style>
</head>
<body>
<main class="canvas">

  <section class="card card--front" aria-label="Business card front">
    <svg class="card__shapes" width="1200" height="687" viewBox="0 0 1200 687" aria-hidden="true">
      <polygon points="520,0 1200,0 1200,16" fill="var(--electric-blue)"/>
      <polygon points="0,663 1200,491 1200,687 0,687" fill="var(--electric-blue)"/>
      <circle cx="1050" cy="318" r="128" fill="var(--electric-blue)"/>
    </svg>
    <div class="brand">
      <span class="brand__primary">VOLTRA</span>
      <span class="brand__secondary">POWER SERVICES</span>
    </div>
    <div class="holder">
      <h1 class="holder__name">SAM RIVERS</h1>
      <p class="holder__location">SYDNEY, AUSTRALIA</p>
      <p class="holder__phone">0400 118 352</p>
    </div>
  </section>

  <section class="card card--back" aria-label="Business card back">
    <div class="contact">
      <p class="contact__email">voltrapower@services.com</p>
      <div class="contact__rule"></div>
      <p class="contact__web">www.voltrapower.com</p>
    </div>
  </section>

</main>
</body>
</html>
```